VelloTask Business Card

Our company is called VelloTask and we are based in Tel Aviv, Israel. We create innovative and exciting methods for getting people on the web engaged with content. We need a cool yet professional business card that will represent our management level employees. keep in mind this is a start up company with a young atmosphere. You can be inspired by our logo (file attached, make sure you have the right font "Ubuntu-Condensed") Use the colors that are used in the logo and create a colourful and professional business card.

```html
<!DOCTYPE html>
<html lang="en">
<head>
<meta charset="utf-8">
<title>VelloTask Business Card</title>
<link rel="stylesheet" href="https://fonts.googleapis.com/css2?family=Ubuntu+Condensed&family=Ubuntu:wght@400&display=swap">
<style>
  :root {
    --backdrop: #e9e7e4;
    --card: #ffffff;
    --ink: #1b1b1b;
    --brand-blue: #1a86cc;
    --accent-yellow: #f2b705;
    --dot-pink: #e91e76;
    --dot-blue: #5bb5e0;
    --dot-green: #8cc63f;
    --dot-purple: #92278f;
    --dot-yellow: #ffcc11;
    --dot-orange: #f9a93a;
    --icon: #222222;
  }
  html, body {
    margin: 0;
    padding: 0;
    width: 1200px;
    height: 1000px;
    overflow: hidden;
    background: var(--backdrop);
  }
  .canvas {
    position: relative;
    width: 1200px;
    height: 1000px;
  }
  .card {
    position: absolute;
    left: 265px;
    width: 666px;
    height: 397px;
    background: var(--card);
    box-shadow: 0 2px 8px rgba(0,0,0,0.18);
    overflow: hidden;
  }
  .card--front { top: 73px; }
  .card--back { top: 532px; }

  .wordmark {
    position: absolute;
    left: 0;
    right: 0;
    top: 248px;
    display: flex;
    align-items: center;
    justify-content: center;
    gap: 18px;
  }
  .wordmark__dot {
    width: 38px;
    height: 38px;
    border-radius: 50%;
    background: var(--dot-pink);
  }
  .wordmark__name {
    font-family: "Ubuntu Condensed", "Ubuntu", sans-serif;
    font-size: 84px;
    line-height: 1;
    color: var(--brand-blue);
    letter-spacing: 0.5px;
  }

  .contact {
    position: absolute;
    left: 33px;
    top: 84px;
    font-family: "Ubuntu Condensed", "Ubuntu", sans-serif;
  }
  .contact__name {
    margin: 0;
    font-size: 26px;
    font-weight: 400;
    color: var(--brand-blue);
    letter-spacing: 0.3px;
    line-height: 1.1;
  }
  .contact__role {
    margin: 4px 0 0;
    font-size: 17px;
    color: var(--brand-blue);
  }
  .contact__list {
    list-style: none;
    margin: 30px 0 0;
    padding: 0;
  }
  .contact__item {
    display: flex;
    align-items: center;
    gap: 8px;
    height: 32.5px;
    font-size: 17px;
    color: var(--accent-yellow);
  }
  .contact__icon {
    width: 15px;
    height: 15px;
    flex: none;
    fill: var(--icon);
  }

  .dot-field {
    position: absolute;
    right: 0;
    top: 0;
    width: 300px;
    height: 397px;
    background:
      radial-gradient(circle at 80% 15%, rgba(146,39,143,0.55), transparent 40%),
      radial-gradient(circle at 35% 30%, rgba(255,204,17,0.55), transparent 40%),
      radial-gradient(circle at 85% 55%, rgba(233,30,118,0.55), transparent 40%),
      radial-gradient(circle at 25% 65%, rgba(91,181,224,0.55), transparent 40%),
      radial-gradient(circle at 50% 90%, rgba(255,204,17,0.55), transparent 40%),
      radial-gradient(circle at 60% 45%, rgba(140,198,63,0.45), transparent 40%),
      linear-gradient(90deg, rgba(255,255,255,1) 0%, rgba(249,169,58,0.25) 40%, rgba(146,39,143,0.25) 100%);
  }
</style>
</head>
<body>
<main class="canvas">
  <section class="card card--front" aria-label="Card front">
    <div class="wordmark">
      <span class="wordmark__dot"></span>
      <span class="wordmark__name">VelloTask</span>
    </div>
  </section>

  <section class="card card--back" aria-label="Card back">
    <div class="contact">
      <h1 class="contact__name">DANA LEVRAN</h1>
      <p class="contact__role">Managing Director</p>
      <ul class="contact__list">
        <li class="contact__item">
          <svg class="contact__icon" viewBox="0 0 16 16" aria-hidden="true"><path d="M2 5c0-2 2-3 6-3s6 1 6 3v1.5h-3.5V5h-5v1.5H2z"/><path d="M4 8h8l2 5H2z"/></svg>
          +972 3 555 0142
        </li>
        <li class="contact__item">
          <svg class="contact__icon" viewBox="0 0 16 16" aria-hidden="true"><path d="M1 3h14v10H1z M2.5 4.5v.3L8 9l5.5-4.2v-.3z" fill-rule="evenodd"/></svg>
          dana@vellotask.com
        </li>
        <li class="contact__item">
          <svg class="contact__icon" viewBox="0 0 16 16" aria-hidden="true"><circle cx="8" cy="8" r="6.5" fill="none" stroke="#222" stroke-width="1.5"/><path d="M1.5 8h13M8 1.5c-3 3.5-3 9.5 0 13M8 1.5c3 3.5 3 9.5 0 13" fill="none" stroke="#222" stroke-width="1.2"/></svg>
          www.vellotask.com
        </li>
        <li class="contact__item">
          <svg class="contact__icon" viewBox="0 0 16 16" aria-hidden="true"><path d="M8 1a5 5 0 0 0-5 5c0 4 5 9 5 9s5-5 5-9a5 5 0 0 0-5-5zm0 7a2 2 0 1 1 0-4 2 2 0 0 1 0 4z"/></svg>
          14 Harbor Lane Tel Aviv 6100
        </li>
        <li class="contact__item">
          <svg class="contact__icon" viewBox="0 0 16 16" aria-hidden="true"><circle cx="8" cy="8" r="6"/></svg>
          Linkspace.com/vellotask
        </li>
      </ul>
    </div>
    <div class="dot-field" role="img" aria-label="Decorative cluster of colourful circles in pink, blue, green, purple, yellow and orange"></div>
  </section>
</main>
</body>
</html>
```